iOS7 test prep app

I need 3 basic screens and 2 product images for an iOS7 app I am prototyping. I provided lots of detail in the attached brief. This is an education product, so warm colors (especially reds) work best.

If you've done flat design for mobile products, please take a look ... Thanks!

Greetings, all. Thank you for your submissions. I am meeting with my product development team this week to review your submissions, and will select a designer before the end of the week. I appreciate your patience with my process, and thank you again for your interest in my project. I'll be back to you soon ... -Dorian

```html
<!DOCTYPE html>
<html lang="en">
<head>
<meta charset="utf-8">
<title>Lumo Prep – Products</title>
<link href="https://fonts.googleapis.com/css2?family=Roboto+Condensed:wght@300;400&family=Open+Sans:wght@400;600&display=swap" rel="stylesheet">
<style>
  :root{
    --red:#ee1d23;
    --green:#21b33b;
    --green-card:rgba(33,170,52,.88);
    --bar:#131313;
    --status:#000;
    --card:rgba(38,34,32,.86);
    --card-edge:rgba(255,255,255,.07);
    --white:#fff;
    --muted:#a7a7a7;
  }
  *{box-sizing:border-box;margin:0;padding:0}
  html,body{width:721px;height:1200px;overflow:hidden;background:#fff}
  .screen{position:relative;width:721px;height:1200px;background:#2d2926;overflow:hidden;font-family:"Open Sans",sans-serif}
  .backdrop{position:absolute;left:0;top:264px;width:721px;height:936px;
    background:radial-gradient(ellipse at 60% 30%,#8a7a66 0%,#5a4c40 35%,#2e2824 75%),#2e2824;opacity:.9}
  .status-bar{position:relative;height:50px;background:var(--status);color:var(--white);display:flex;align-items:center;padding:0 10px;font-weight:600;font-size:26px;font-family:"Open Sans",sans-serif}
  .carrier{display:flex;align-items:flex-end;gap:10px;font-size:25px}
  .signal{display:flex;align-items:flex-end;gap:3px}
  .signal span{width:5px;background:#fff;display:block}
  .clock{position:absolute;left:50%;transform:translateX(-50%);font-size:28px}
  .status-icons{margin-left:auto;display:flex;gap:12px;align-items:center}
  .app-header{position:relative;height:106px;background:var(--red);display:flex;align-items:center;justify-content:center}
  .app-title{font-family:"Roboto Condensed",sans-serif;font-weight:400;font-size:50px;color:var(--white)}
  .back-btn{position:absolute;left:30px;top:36px}
  .menu-btn{position:absolute;right:30px;top:40px}
  .section-bar{position:relative;height:108px;background:var(--bar);display:flex;align-items:center;padding:0 32px;justify-content:space-between}
  .section-title{font-family:"Roboto Condensed",sans-serif;font-weight:400;font-size:38px;color:var(--green)}
  .product-list{position:absolute;top:282px;left:22px;width:677px;display:flex;flex-direction:column;gap:6px;list-style:none}
  .product{height:176px;background:var(--card);border-radius:3px;border:1px solid var(--card-edge);display:flex;align-items:flex-start;padding:18px 18px}
  .product.is-active{background:var(--green-card)}
  .thumb{position:relative;width:196px;height:152px;flex:none;border:2px solid rgba(255,255,255,.85);border-radius:2px}
  .is-active .thumb{border-color:rgba(255,255,255,.35);filter:brightness(.7)}
  .zoom{position:absolute;left:72px;top:50px}
  .info{margin-left:24px;padding-top:6px}
  .info h3{font-family:"Roboto Condensed",sans-serif;font-weight:400;font-size:29px;color:var(--green);line-height:1.1}
  .is-active .info h3{color:var(--white)}
  .info h4{font-weight:600;font-size:16px;color:var(--white);margin-top:12px}
  .info p{font-size:13.5px;color:var(--muted);line-height:27px;margin-top:8px;width:410px}
  .is-active .info p{color:#e6f5e6}
</style>
</head>
<body>
<div class="screen">
  <div class="backdrop" role="img" aria-label="Blurred family photograph in warm brown tones behind the list"></div>

  <div class="status-bar">
    <div class="carrier">
      <div class="signal"><span style="height:7px"></span><span style="height:10px"></span><span style="height:13px"></span><span style="height:16px"></span><span style="height:19px"></span></div>
      Vela
    </div>
    <div class="clock">4:20 PM</div>
    <div class="status-icons">
      <svg width="24" height="24" viewBox="0 0 24 24"><circle cx="12" cy="12" r="11" fill="#fff"/><path d="M12 6v6h4" stroke="#000" stroke-width="2.4" fill="none"/></svg>
      <svg width="24" height="24" viewBox="0 0 24 24"><path d="M22 2L2 11l9 2 2 9z" fill="#fff"/></svg>
      <svg width="34" height="28" viewBox="0 0 34 28"><path d="M27 14a12 12 0 1 1-4-9" stroke="#fff" stroke-width="2.6" fill="none"/><path d="M25 1l-1 7 7-2z" fill="#fff"/><rect x="9" y="12" width="10" height="8" fill="#fff"/><path d="M11 12v-3a3 3 0 0 1 6 0v3" stroke="#fff" stroke-width="2" fill="none"/></svg>
      <svg width="50" height="22" viewBox="0 0 50 22"><rect x="1" y="1" width="44" height="20" rx="2" stroke="#fff" stroke-width="2" fill="none"/><rect x="4" y="4" width="38" height="14" fill="#fff"/><rect x="46" y="7" width="3" height="8" fill="#fff"/></svg>
    </div>
  </div>

  <header class="app-header">
    <svg class="back-btn" width="22" height="40" viewBox="0 0 22 40"><path d="M19 2L3 20l16 18" stroke="#fff" stroke-width="4" fill="none"/></svg>
    <h1 class="app-title">Lumo Prep</h1>
    <svg class="menu-btn" width="46" height="28" viewBox="0 0 46 28"><g fill="#fff"><rect y="0" width="46" height="4"/><rect y="12" width="46" height="4"/><rect y="24" width="46" height="4"/></g></svg>
  </header>

  <div class="section-bar">
    <h2 class="section-title">PRODUCTS</h2>
    <svg width="18" height="32" viewBox="0 0 18 32"><path d="M2 2l13 14L2 30" stroke="#21b33b" stroke-width="3" fill="none"/></svg>
  </div>

  <ul class="product-list">
    <li class="product is-active">
      <div class="thumb" role="img" aria-label="Family sitting together on a sofa" style="background:linear-gradient(135deg,#c9b8a4,#8d7562 60%,#5a4a3e)">
        <svg class="zoom" width="48" height="48" viewBox="0 0 48 48"><circle cx="24" cy="24" r="24" fill="rgba(0,0,0,.75)"/><circle cx="22" cy="22" r="9" stroke="#21b33b" stroke-width="2.5" fill="none"/><path d="M28.5 28.5l7 7M22 17.5v9M17.5 22h9" stroke="#21b33b" stroke-width="2.5"/></svg>
      </div>
      <div class="info">
        <h3>Lorem ipsum dolor sit amet</h3>
        <h4>Lorem ipsum dolor sit amet</h4>
        <p>Consectetur adipiscing elit. Praesent malesuada tincidunt nibh, eget fermentum lacus molestie.</p>
      </div>
    </li>
    <li class="product">
      <div class="thumb" role="img" aria-label="Students studying with a tablet in a library" style="background:linear-gradient(135deg,#d8d2c8,#b49a86 50%,#6f7a92)"></div>
      <div class="info">
        <h3>Lorem ipsum dolor sit amet</h3>
        <h4>Lorem ipsum dolor sit amet</h4>
        <p>Consectetur adipiscing elit. Praesent malesuada tincidunt nibh, eget fermentum lacus molestie.</p>
      </div>
    </li>
    <li class="product">
      <div class="thumb" role="img" aria-label="Mother and daughter reading on the floor at home" style="background:linear-gradient(135deg,#e6d6c0,#c9a98a 50%,#8e7a6a)"></div>
      <div class="info">
        <h3>Lorem ipsum dolor sit amet</h3>
        <h4>Lorem ipsum dolor sit amet</h4>
        <p>Consectetur adipiscing elit. Praesent malesuada tincidunt nibh, eget fermentum lacus molestie.</p>
      </div>
    </li>
    <li class="product">
      <div class="thumb" role="img" aria-label="Smiling family with their dog" style="background:linear-gradient(135deg,#f4f1ee,#c69c78 55%,#3f4f7a)"></div>
      <div class="info">
        <h3>Lorem ipsum dolor sit amet</h3>
        <h4>Lorem ipsum dolor sit amet</h4>
        <p>Consectetur adipiscing elit. Praesent malesuada tincidunt nibh, eget fermentum lacus molestie.</p>
      </div>
    </li>
    <li class="product">
      <div class="thumb" role="img" aria-label="Family sitting together on a sunny beach" style="background:linear-gradient(135deg,#9fc8e6,#e7c79a 50%,#d98a52)"></div>
      <div class="info">
        <h3>Lorem ipsum dolor sit amet</h3>
        <h4>Lorem ipsum dolor sit amet</h4>
        <p>Consectetur adipiscing elit. Praesent malesuada tincidunt nibh, eget fermentum lacus molestie.</p>
      </div>
    </li>
  </ul>
</div>
</body>
</html>
```